wedding DJ & Lighting entertainment

We are a DJ and Lighting production company. We specialize mainly in wedding entertainment. I've attached my old postcard in the image folder, however, i would like something new and updated. You can use the same bullet points from the front page, but i would like to have a cleaner look on the front. I'd like to have one large image on the front side and smaller images on the back side. I'd also like to have some text below the logo. I'd like it to say DJ * Lighting * Audio/Visual. I'd also like to have the phrase "Celebrate with Style"

Target Market(s)

weddings, private events, women

Industry/Entity Type

It Company

Font styles to use
Sans Serif
Script

Requirements
Must have
• look elegant, sophisticated. Must have my new logo! My logo is attached as one of the files. It's a headphone logo.

```html
<!DOCTYPE html>
<html lang="en">
<head>
<meta charset="utf-8">
<title>Velvet Echo Events – Postcard</title>
<link href="https://fonts.googleapis.com/css2?family=Questrial&family=Pinyon+Script&display=swap" rel="stylesheet">
<style>
  :root{
    --page:#ffffff;
    --ink:#333038;
    --ink-soft:#5c5a60;
    --accent:#e0262b;
    --white:#ffffff;
    --violet-deep:#2a0f3a;
    --mauve:#b88aa0;
    --mauve-light:#d9b6c6;
    --panel-top:#d6cdd6;
    --panel-bottom:#f7f2f5;
  }
  *{box-sizing:border-box;margin:0;padding:0}
  html,body{width:786px;height:1200px;overflow:hidden;background:var(--page)}
  body{position:relative;font-family:"Questrial",Arial,sans-serif;color:var(--ink)}

  .card{position:absolute;left:30px;width:726px;height:562px;overflow:hidden;
    box-shadow:0 3px 10px rgba(0,0,0,.35)}
  .card--front{top:29px}
  .card--back{top:609px;background:linear-gradient(180deg,var(--panel-top) 0%,var(--panel-bottom) 60%,#ece3e9 100%)}

  /* front */
  .hero-photo{position:absolute;inset:0;
    background:
      radial-gradient(ellipse 260px 140px at 560px 500px,rgba(243,233,160,.9),rgba(243,233,160,0) 100%),
      radial-gradient(ellipse 200px 160px at 160px 380px,rgba(245,235,220,.75),rgba(245,235,220,0) 100%),
      radial-gradient(ellipse 300px 200px at 470px 110px,rgba(194,58,184,.65),rgba(194,58,184,0) 100%),
      linear-gradient(180deg,var(--violet-deep) 0%,#3a1a30 45%,#6a4a2a 75%,#b89a50 100%)}
  .services{position:absolute;left:308px;top:85px;list-style:none;color:var(--white);
    font-size:25px;line-height:29px;white-space:nowrap;text-shadow:0 1px 3px rgba(0,0,0,.7)}
  .slogan{position:absolute;left:350px;top:238px;font-family:"Pinyon Script",cursive;
    font-size:40px;color:var(--white);white-space:nowrap;text-shadow:0 2px 4px rgba(0,0,0,.7)}

  .brand{position:absolute;text-align:center}
  .brand__name{display:flex;align-items:center;justify-content:center;gap:10px;
    font-size:36px;color:var(--ink);letter-spacing:.5px;white-space:nowrap}
  .brand__dot{width:16px;height:16px;border-radius:50%;background:var(--accent)}
  .brand__tag{margin-top:16px;font-size:18px;color:var(--ink-soft);white-space:nowrap}
  .card--front .brand{left:380px;top:432px;width:300px}

  /* back */
  .intro{position:absolute;left:46px;top:50px;font-size:19px;line-height:28px;
    font-style:italic;color:var(--ink);white-space:nowrap}
  .card--back .brand{left:60px;top:326px;width:300px}
  .contact{position:absolute;left:60px;top:427px;width:300px;list-style:none;text-align:center;
    font-size:19px;line-height:28px;color:var(--ink-soft)}
  .contact li{display:flex;align-items:center;justify-content:center;gap:6px;white-space:nowrap}
  .contact svg{width:15px;height:15px;stroke:var(--ink-soft);fill:none;stroke-width:1.4}

  .gallery{position:absolute;left:432px;top:0;width:294px;height:562px}
  .gallery__photo{position:absolute;left:0;width:294px}
  .gallery__photo--tables{top:0;height:200px;
    background:radial-gradient(ellipse 90px 60px at 110px 110px,#d8d0f0,rgba(216,208,240,0) 100%),
      linear-gradient(180deg,#5a3aa8,#2a1a60)}
  .gallery__photo--dance{top:200px;height:192px;
    background:radial-gradient(ellipse 160px 50px at 150px 20px,#f04ab0,rgba(240,74,176,0) 100%),
      linear-gradient(180deg,#c8307a,#3a1a30 70%,#5a4a40)}
  .gallery__photo--hall{top:392px;height:170px;
    background:radial-gradient(ellipse 120px 50px at 150px 140px,#c0a8d8,rgba(192,168,216,0) 100%),
      linear-gradient(180deg,#6a8ad0,#4a3a9a 50%,#2a1a50)}
  .sweep{position:absolute;left:380px;top:0;width:120px;height:562px}
</style>
</head>
<body>

<section class="card card--front">
  <div class="hero-photo" role="img" aria-label="Bride and groom sharing their first dance in a ballroom washed in purple uplighting"></div>
  <ul class="services">
    <li>DJ &amp; Emcee Entertainment</li>
    <li>Customized Lighting Décor</li>
    <li>Event Hosting &amp; Coordination</li>
    <li>Helpful Planning Tools</li>
    <li>Personalized Service</li>
  </ul>
  <p class="slogan">Celebrate with Style</p>
  <div class="brand">
    <p class="brand__name"><span class="brand__dot"></span>Velvet Echo Events</p>
    <p class="brand__tag">DJ ✦ Lighting ✦ Audio/Visual</p>
  </div>
</section>

<section class="card card--back">
  <p class="intro">With years of entertainment and<br>production experience, we make<br>sure your occasion comes to life<br>for you and your guests. After all,<br>it’s your day, your event, and your<br>memories … it’s about you.</p>

  <div class="brand">
    <p class="brand__name"><span class="brand__dot"></span>Velvet Echo Events</p>
    <p class="brand__tag">DJ ✦ Lighting ✦ Audio/Visual</p>
  </div>

  <ul class="contact">
    <li><svg viewBox="0 0 16 16"><circle cx="8" cy="8" r="6.5"/><path d="M8 7v4.5M8 4.6v.6"/></svg>velvetechoevents.com</li>
    <li><svg viewBox="0 0 16 16"><rect x="1.5" y="3.5" width="13" height="9"/><path d="M1.5 3.5 8 9l6.5-5.5"/></svg>hello@velvetechoevents.com</li>
    <li><svg viewBox="0 0 16 16"><circle cx="8" cy="8" r="6.5"/><path d="M5.5 5c0 3 2.5 5.5 5.5 5.5"/></svg>888-555-0142</li>
  </ul>

  <div class="gallery">
    <div class="gallery__photo gallery__photo--tables" role="img" aria-label="Reception tables with floral centrepiece under violet lighting"></div>
    <div class="gallery__photo gallery__photo--dance" role="img" aria-label="Guests dancing with raised hands under pink lights"></div>
    <div class="gallery__photo gallery__photo--hall" role="img" aria-label="Ballroom with blue uplighting and a monogrammed dance floor"></div>
  </div>

  <svg class="sweep" viewBox="0 0 120 562" preserveAspectRatio="none" aria-hidden="true">
    <path d="M52 0 C 30 180, 30 380, 120 562 L 60 562 C 10 400, 10 180, 36 0 Z" fill="var(--mauve)"/>
    <path d="M36 0 C 10 180, 10 400, 60 562" stroke="var(--mauve-light)" stroke-width="4" fill="none"/>
    <path d="M58 0 C 38 180, 38 380, 120 545" stroke="var(--mauve-light)" stroke-width="3" fill="none"/>
    <path d="M44 0 C 20 180, 20 390, 90 562" stroke="#ffffff" stroke-opacity=".6" stroke-width="2" fill="none"/>
  </svg>
</section>

</body>
</html>
```